Buff & Gleam

polished concrete and epoxy coatings flooring company

Target Market(s)

Industrial commercial

Industry/Entity Type

Industrial flooring contractor

Contact Information for Business Card

POLISHED CONCRETE • EPOXY COATING • TERRAZZO RESTORATION • SHOT BLASTING • SURFACE PREPARATION • JOINT FILLING • TILE/ CARPET /GLUE REMOVAL

Colors
0054AA
0677BA
7BADD7
CADEEF
E8F1F8

Requirements
Must have
• email buffandgleamfloors@mailbrook.example Address 47215 Tallowmere Rd, Fraser, MI 48093. Name Ray Tulvin. Services Polished concrete- Epoxy Coatings- Terrazzo restoration-surface preparation- safety striping- joint filling- tile/ carpet/ glue removal phone number 586-700-3926 email buffandgleamfloors.example
Nice to have
• Instagram Facebook logo maybe smaller in the corner

```html
<!DOCTYPE html>
<html lang="en">
<head>
<meta charset="utf-8">
<title>Buff &amp; Gleam — Business Card</title>
<link href="https://fonts.googleapis.com/css2?family=Montserrat:wght@400;500;700&display=swap" rel="stylesheet">
<style>
  :root {
    --backdrop: #bdbdbd;
    --card: #000000;
    --blue-deep: #0054AA;
    --blue-mid: #0677BA;
    --blue-soft: #7BADD7;
    --blue-pale: #CADEEF;
    --blue-mist: #E8F1F8;
    --ink-dark: #0d1a2a;
    --ink-light: #ffffff;
  }
  * { margin: 0; padding: 0; box-sizing: border-box; }
  html, body { width: 1200px; height: 1200px; overflow: hidden; }
  body {
    background: var(--backdrop);
    font-family: "Montserrat", Arial, sans-serif;
    position: relative;
  }
  .card {
    position: absolute;
    left: 150px;
    width: 898px;
    height: 525px;
    background: var(--card);
    box-shadow: 0 3px 10px rgba(0,0,0,0.35);
    overflow: hidden;
  }
  .card--front { top: 55px; }
  .card--back { top: 621px; }

  .stripe {
    position: absolute;
    top: 0;
    width: 7px;
    height: 100%;
    background: var(--blue-soft);
  }
  .name-band {
    position: absolute;
    left: 0;
    top: 211px;
    width: 341px;
    height: 103px;
    background: var(--blue-pale);
    padding: 16px 0 0 76px;
    color: var(--ink-dark);
  }
  .name-band__name {
    font-weight: 700;
    font-size: 30px;
    letter-spacing: 0.5px;
    line-height: 1.2;
    white-space: nowrap;
    color: var(--blue-deep);
  }
  .name-band__role {
    font-weight: 400;
    font-size: 21px;
    margin-top: 4px;
  }

  .brand-block {
    position: absolute;
    top: 0;
    display: flex;
    align-items: center;
    justify-content: center;
    background: radial-gradient(circle at 40% 35%, var(--blue-mist), var(--blue-soft));
    color: var(--blue-deep);
    font-weight: 700;
    text-align: center;
    line-height: 1.1;
  }
  .card--front .brand-block { left: 458px; width: 286px; height: 245px; font-size: 40px; }
  .card--back .brand-block { left: 239px; width: 421px; height: 357px; font-size: 58px; }

  .contact-list {
    position: absolute;
    left: 442px;
    top: 292px;
    list-style: none;
    color: var(--ink-light);
    font-size: 18px;
  }
  .contact-list li {
    display: flex;
    align-items: center;
    height: 35px;
    white-space: nowrap;
  }
  .contact-list li.contact-list__web { margin-top: 19px; }
  .contact-list svg {
    width: 18px;
    height: 18px;
    fill: var(--blue-pale);
    margin-right: 14px;
    flex: none;
  }

  .services {
    position: absolute;
    left: 40px;
    right: 40px;
    top: 393px;
    text-align: center;
    color: var(--ink-light);
    font-weight: 500;
    font-size: 19.5px;
    line-height: 25px;
  }
</style>
</head>
<body>

<section class="card card--front">
  <div class="stripe" style="left:56px"></div>
  <div class="stripe" style="left:76px"></div>
  <div class="stripe" style="left:96px"></div>
  <div class="stripe" style="left:116px"></div>

  <div class="name-band">
    <div class="name-band__name">RAY TULVIN</div>
    <div class="name-band__role">Manager</div>
  </div>

  <div class="brand-block">Buff &amp;<br>Gleam</div>

  <ul class="contact-list">
    <li>
      <svg viewBox="0 0 24 24"><path d="M7 1h10a2 2 0 0 1 2 2v18a2 2 0 0 1-2 2H7a2 2 0 0 1-2-2V3a2 2 0 0 1 2-2zm0 3v14h10V4zm5 15.5a1 1 0 1 0 0 2 1 1 0 0 0 0-2z"/></svg>
      586-700-3926
    </li>
    <li>
      <svg viewBox="0 0 24 24"><path d="M6.6 10.8a15.2 15.2 0 0 0 6.6 6.6l2.2-2.2a1 1 0 0 1 1-.25 11.4 11.4 0 0 0 3.6.57 1 1 0 0 1 1 1V20a1 1 0 0 1-1 1A17 17 0 0 1 3 4a1 1 0 0 1 1-1h3.5a1 1 0 0 1 1 1c0 1.25.2 2.45.57 3.57a1 1 0 0 1-.25 1z"/></svg>
      586-700-4810
    </li>
    <li>
      <svg viewBox="0 0 24 24"><path d="M3 5h18a1 1 0 0 1 1 1v12a1 1 0 0 1-1 1H3a1 1 0 0 1-1-1V6a1 1 0 0 1 1-1zm1 2.4V17h16V7.4l-8 5z"/></svg>
      buffandgleamfloors@mailbrook.example
    </li>
    <li>
      <svg viewBox="0 0 24 24"><path d="M12 2a7 7 0 0 1 7 7c0 5.2-7 13-7 13S5 14.2 5 9a7 7 0 0 1 7-7zm0 4.5a2.5 2.5 0 1 0 0 5 2.5 2.5 0 0 0 0-5z"/></svg>
      47215 Tallowmere Rd, Fraser, MI 48093
    </li>
    <li class="contact-list__web">
      <svg viewBox="0 0 24 24"><path d="M12 2a10 10 0 1 1 0 20 10 10 0 0 1 0-20zm-1 2.1A8 8 0 0 0 4.1 11H8a15 15 0 0 1 3-6.9zm2 0a15 15 0 0 1 3 6.9h3.9A8 8 0 0 0 13 4.1zM12 4.6A13 13 0 0 0 10 11h4a13 13 0 0 0-2-6.4zM4.1 13A8 8 0 0 0 11 19.9 15 15 0 0 1 8 13zm5.9 0a13 13 0 0 0 2 6.4 13 13 0 0 0 2-6.4zm6 0a15 15 0 0 1-3 6.9 8 8 0 0 0 6.9-6.9z"/></svg>
      buffandgleamfloors.example
    </li>
  </ul>
</section>

<section class="card card--back">
  <div class="brand-block">Buff &amp;<br>Gleam</div>
  <p class="services">
    POLISHED CONCRETE • EPOXY COATING • TERRAZZO RESTORATION<br>
    • SHOT BLASTING • SURFACE PREPARATION • JOINT FILLING • TILE/<br>
    CARPET /GLUE REMOVAL
  </p>
</section>

</body>
</html>
```